Supplement Company Needs A New Label Design

My company is looking to increase the appeal of our supplement labels. We need to keep the logo the same, the name the same, and the overall information all the same. We wouldn't mind adding the following, or changing colour schemes/fonts to increase shelf appeal.

Helps To:

- Increase Bioavailability of Nutrients

- Regulate Blood Sugar Levels

- Reduce Body Fat

- Increase Insulin Sensitivity

The label needs to be roughly 3inches high and 8inches around.

About Us:
Scientifically backed formulas with studies linked back to each ingredient. No "proprietary blends" just pure transparency.

We have another product that will need to be done too, so the winner could be chosen for the secondary project as well.

Target Market(s)

Those looking to lose weight and regulate their blood sugar. This product can be used from those looking to pack muscle on while losing fat, or by diabetics looking to control blood sugar and weight.

Industry/Entity Type

Supplement

Requirements
Must have
• My project must have an appeal that draws people when they see it on a shelf. Something that will differentiate it from my competitors. It must also have "Helps to" if including the things it does. This is just to follow FDA guidelines.
Nice to have
• Nice to have a unique kind of font for the name "Gather and Prevail". I tried my best with designing the labels to give a good template to use, however, this is all I am capable of.

```html
<!DOCTYPE html>
<html lang="en">
<head>
<meta charset="utf-8">
<title>Gather and Prevail – Nutrient Partitioner Label</title>
<link href="https://fonts.googleapis.com/css2?family=Russo+One&family=Oswald:wght@400;500&family=Roboto+Condensed:wght@400;700&display=swap" rel="stylesheet">
<style>
  :root {
    --page: #f4f4f4;
    --ink-dark: #1f1f21;
    --silver-light: #d9d9d9;
    --silver-mid: #a9a9ab;
    --gold: #f3c614;
    --white: #ffffff;
    --black: #0c0c0c;
  }
  * { box-sizing: border-box; margin: 0; padding: 0; }
  html, body { width: 1200px; height: 780px; overflow: hidden; background: var(--page); }
  .canvas { position: relative; width: 1200px; height: 780px; }

  .label {
    position: absolute; left: 40px; top: 180px;
    width: 1120px; height: 420px;
    background: var(--ink-dark);
    overflow: hidden;
    box-shadow: 0 10px 30px rgba(0,0,0,.18);
  }
  .label-shapes { position: absolute; inset: 0; }

  .category {
    position: absolute; left: 0; top: 26px; width: 560px; text-align: center;
    font-family: "Roboto Condensed", sans-serif; font-weight: 700;
    font-size: 15px; letter-spacing: .5px; color: var(--black);
  }
  .brand {
    position: absolute; left: 170px; top: 50px; height: 40px; width: 220px;
    display: flex; align-items: center; gap: 10px; padding: 0 12px;
    background: var(--black);
  }
  .brand-square { width: 20px; height: 20px; background: var(--white); flex: none; }
  .brand-name {
    font-family: "Roboto Condensed", sans-serif; font-weight: 700; white-space: nowrap;
    font-size: 17px; line-height: 1; color: var(--white); letter-spacing: 1px;
  }

  .product-name {
    position: absolute; left: 20px; top: 126px; width: 440px; text-align: center;
    font-family: "Russo One", sans-serif; font-weight: 400; color: var(--white); line-height: 1;
  }
  .product-name .word { display: block; font-size: 56px; }
  .product-name .joiner { display: block; font-size: 22px; margin: 6px 0; }

  .runner-art {
    position: absolute; left: 460px; top: 118px; width: 220px; height: 160px;
    background: radial-gradient(closest-side, rgba(243,198,20,.7), rgba(243,198,20,.25) 55%, rgba(243,198,20,0) 100%);
  }

  .helps-to {
    position: absolute; left: 40px; top: 300px;
    font-family: "Oswald", sans-serif; font-weight: 500; font-size: 13px;
    letter-spacing: 1.5px; text-transform: uppercase; color: var(--gold); line-height: 20px;
  }
  .benefits {
    position: absolute; left: 40px; top: 322px; list-style: none;
    font-family: "Oswald", sans-serif; font-weight: 400; font-size: 14px;
    text-transform: uppercase; line-height: 22px; color: var(--white);
  }
  .benefits li::before { content: "➤ "; color: var(--silver-mid); font-size: 10px; }
  .benefits li:nth-child(2) { padding-left: 14px; }
  .benefits li:nth-child(3) { padding-left: 28px; color: var(--black); }
  .benefits li:nth-child(4) { padding-left: 14px; color: var(--black); }
  .benefits li:nth-child(n+3)::before { color: var(--black); }

  .tagline {
    position: absolute; left: 780px; top: 360px; width: 300px;
    transform: rotate(-26.57deg); transform-origin: left top;
    font-family: "Oswald", sans-serif; font-weight: 500; font-size: 14px;
    text-transform: uppercase; color: var(--black); line-height: 18px;
  }
  .count {
    position: absolute; left: 980px; top: 352px; width: 120px; height: 30px;
    border: 2px solid var(--black); border-radius: 50%;
    font-family: "Oswald", sans-serif; font-weight: 500; font-size: 14px;
    text-align: center; line-height: 26px; color: var(--black);
  }
  .supplement-type {
    position: absolute; left: 960px; top: 392px; width: 160px; text-align: center;
    font-family: "Roboto Condensed", sans-serif; font-size: 11px; letter-spacing: 1px;
    color: var(--black);
  }
</style>
</head>
<body>
<div class="canvas">
  <div class="label">
    <svg class="label-shapes" width="1120" height="420" viewBox="0 0 1120 420" aria-hidden="true">
      <defs>
        <linearGradient id="silver" x1="0" y1="0" x2="0" y2="1">
          <stop offset="0" stop-color="#d9d9d9"/>
          <stop offset="1" stop-color="#a9a9ab"/>
        </linearGradient>
      </defs>
      <rect class="band-top" x="0" y="0" width="1120" height="110" fill="url(#silver)"/>
      <polygon class="side-gold" points="620,420 1120,170 1120,270 820,420" fill="#f3c614"/>
      <polygon class="side-silver" points="820,420 1120,270 1120,420" fill="url(#silver)"/>
      <polygon class="benefits-strip" points="0,286 470,286 458,294 0,294" fill="#a9a9ab"/>
      <polygon class="benefits-gold" points="0,364 600,364 575,420 0,420" fill="#f3c614"/>
    </svg>

    <div class="category">NUTRIENT PARTITIONER</div>
    <div class="brand"><span class="brand-square"></span><span class="brand-name">KESTREL NUTRITION</span></div>

    <h1 class="product-name">
      <span class="word">GATHER</span>
      <span class="joiner">AND</span>
      <span class="word">PREVAIL</span>
    </h1>

    <div class="runner-art" role="img" aria-label="Gold particle illustration of a sprinting athlete"></div>

    <p class="helps-to">Helps to:</p>
    <ul class="benefits">
      <li>Increase bioavailability of nutrients</li>
      <li>Regulate blood sugar levels</li>
      <li>Reduce body fat</li>
      <li>Increase insulin sensitivity</li>
    </ul>

    <p class="tagline">For those who want to take control<br>of their body's composition</p>
    <div class="count">60 TABLETS</div>
    <div class="supplement-type">DIETARY SUPPLEMENT</div>
  </div>
</div>
</body>
</html>
```